Corvel Tax Advisers Business Card

We are seeking a clean, professional, and modern double sided business card design for Corvel Tax Advisers, a tax, accounting, and advisory firm serving business owners, professionals, and investors.
The design should convey credibility, precision, trust, and sophistication appropriate for a CPA level tax advisory firm. Avoid playful, trendy, or overly decorative styles. The look should be sharp, balanced, and timeless.
Our official company logo has been uploaded, which must be incorporated appropriately and consistently with the brand. Designers should not modify, distort, or recreate the logo.
Card format
Standard US business card size (3.5 x 2 inches)
Double sided
Design direction
Professional and modern
Minimalist and uncluttered
Strong typography and clean spacing
Subtle visual interest is welcome, but simplicity is preferred
High contrast and readability are critical
Front side
Primary focus on the Corvel Tax Advisers logo
The firm name should be clearly legible and visually prominent
Background may be white or dark, depending on what best complements the logo
Back side
Contact information layout, such as
Name: Martin G. Pellow, MS, CPA, EA
Title: Principal, Tax Services
Email: mpellow@mycorvelfirm.net
Website: https://www.corvelfirm-example.tax/
Mobile: (480) 555-0132
Direct: (817) 555-0187
Main: (817) 555-0149
Address: 3807 Fenwick Rd., Suite 118, Grapevine, TX 76099
Icons may be used sparingly if they enhance clarity
The layout should feel organized and structured
Color and style
Use colors that complement the uploaded logo
Neutral, professional tones preferred
Avoid loud or saturated colors
The design should print well on standard cardstock
Print considerations
Design should be print‑ready
No edge to edge elements that risk being cut off
Proper margins and bleed awareness
Overall, the goal is a polished, high end business card that reflects trust, expertise, and professionalism consistent with a firm providing tax strategy, compliance, and advisory services.

```html
<!DOCTYPE html>
<html lang="en">
<head>
<meta charset="utf-8">
<title>Quillmere Tax Advisers – Business Card</title>
<link href="https://fonts.googleapis.com/css2?family=Inter:wght@400;500;700;800&family=Montserrat:wght@400;500;700&display=swap" rel="stylesheet">
<style>
  :root {
    --navy: #1f2358;
    --orange: #f07022;
    --paper: #f5f5f7;
    --white: #ffffff;
    --backdrop: #d9dbe0;
    --card-shadow: 0 18px 40px rgba(31, 35, 88, 0.18);
  }
  * { box-sizing: border-box; margin: 0; padding: 0; }
  html, body {
    width: 1200px;
    height: 1113px;
    overflow: hidden;
    background: var(--backdrop);
  }
  .sheet {
    width: 1200px;
    height: 1113px;
    display: flex;
    flex-direction: column;
    align-items: center;
    justify-content: center;
    gap: 72px;
  }
  .card {
    width: 700px;
    height: 400px;
    background: var(--paper);
    box-shadow: var(--card-shadow);
    position: relative;
    overflow: hidden;
  }

  /* Front */
  .card--front {
    display: flex;
    flex-direction: column;
    align-items: center;
    justify-content: center;
  }
  .brand {
    display: flex;
    align-items: center;
    gap: 20px;
    margin-top: -40px;
  }
  .brand__square {
    width: 24px;
    height: 24px;
    background: var(--navy);
  }
  .brand__name {
    font-family: "Montserrat", sans-serif;
    font-weight: 700;
    font-size: 36px;
    letter-spacing: 0.08em;
    color: var(--navy);
    text-transform: uppercase;
    white-space: nowrap;
  }
  .services {
    position: absolute;
    bottom: 62px;
    left: 0;
    right: 0;
    display: flex;
    justify-content: center;
    align-items: center;
    gap: 22px;
    font-family: "Montserrat", sans-serif;
    font-weight: 500;
    font-size: 15px;
    letter-spacing: 0.2em;
    color: var(--navy);
  }
  .services__divider {
    width: 2px;
    height: 16px;
    background: var(--orange);
  }

  /* Back */
  .card--back {
    display: grid;
    grid-template-columns: 40% 60%;
    font-family: "Inter", sans-serif;
  }
  .web-panel {
    display: flex;
    flex-direction: column;
    justify-content: flex-end;
    padding: 0 0 58px 32px;
    gap: 6px;
  }
  .web-panel__email {
    font-size: 14px;
    color: var(--navy);
    white-space: nowrap;
  }
  .web-panel__site {
    font-size: 17px;
    color: var(--orange);
    white-space: nowrap;
  }
  .contact-panel {
    background: var(--navy);
    padding: 54px 36px 0 48px;
    color: var(--white);
  }
  .person__name {
    font-weight: 800;
    font-size: 38px;
    color: var(--orange);
    line-height: 1.05;
    white-space: nowrap;
  }
  .person__credentials {
    font-size: 17px;
    color: var(--orange);
    margin-top: 6px;
  }
  .person__title {
    font-size: 15px;
    margin-top: 4px;
  }
  .phones {
    list-style: none;
    margin-top: 42px;
    font-size: 18px;
    line-height: 1.45;
  }
  .phones__label {
    color: var(--orange);
    font-weight: 700;
  }
  .address {
    font-style: normal;
    font-size: 14px;
    line-height: 1.35;
    margin-top: 26px;
  }
</style>
</head>
<body>
<main class="sheet">
  <section class="card card--front" aria-label="Card front">
    <div class="brand">
      <span class="brand__square" aria-hidden="true"></span>
      <span class="brand__name">Quillmere Tax Advisers</span>
    </div>
    <p class="services">
      <span>TAX STRATEGY</span>
      <span class="services__divider" aria-hidden="true"></span>
      <span>COMPLIANCE</span>
      <span class="services__divider" aria-hidden="true"></span>
      <span>ADVISORY</span>
    </p>
  </section>

  <section class="card card--back" aria-label="Card back">
    <div class="web-panel">
      <span class="web-panel__email">mpellow@myquillmere.net</span>
      <span class="web-panel__site">www.quillmere-example.tax</span>
    </div>
    <div class="contact-panel">
      <h1 class="person__name">Martin G. Pellow</h1>
      <p class="person__credentials">MS, CPA, EA</p>
      <p class="person__title">Principal, Tax Services</p>
      <ul class="phones">
        <li><span class="phones__label">Mobile :</span> (480) 555-0132</li>
        <li><span class="phones__label">Direct :</span> (817) 555-0187</li>
        <li><span class="phones__label">Main:</span> (817) 555-0149</li>
      </ul>
      <address class="address">3807 Fenwick Rd., Suite 118,<br>Millbrook, TX 76099</address>
    </div>
  </section>
</main>
</body>
</html>
```